Business Card design for Brightvale Global

we need a business card design for our company. we are a trading company based in LA.

Company Name: Brightvale Global Corp.
Contact: Marcus Ortega
Title: CEO
Tel: 310-647-2093
Email: bvgcorp7@mailnest.example

Target Market(s)

International, especially China

Industry/Entity Type

Trade

Colors
3276b5
34a7d8
0555a3
0493ce
85cae6
85acd3
d0dfed
cee9f5

Requirements
Must have
• Logo and contact, to have international/global feeling

```html
<!DOCTYPE html>
<html lang="en">
<head>
<meta charset="utf-8">
<title>Brightvale Global – Business Card</title>
<link rel="stylesheet" href="https://fonts.googleapis.com/css2?family=Questrial&family=PT+Sans:wght@700&display=swap">
<style>
  :root {
    --backdrop: #2a2a2c;
    --blue-deep: #0b3f73;
    --blue-mid: #0555a3;
    --blue-bright: #29a9e0;
    --navy: #1d3a66;
    --sky: #3a8fd0;
    --paper: #f3f3f3;
    --grey-text: #555a60;
    --white: #ffffff;
  }
  * { margin: 0; padding: 0; box-sizing: border-box; }
  html, body { width: 1200px; height: 960px; overflow: hidden; }
  body {
    background: var(--backdrop);
    position: relative;
    font-family: "Questrial", "Century Gothic", sans-serif;
  }
  .card {
    position: absolute;
    left: 320px;
    width: 600px;
    height: 342px;
    border-radius: 20px;
    overflow: hidden;
  }
  .card--front {
    top: 108px;
    background: radial-gradient(ellipse 340px 260px at 630px 290px, var(--blue-bright) 0%, var(--blue-mid) 55%, var(--blue-deep) 100%);
  }
  .card--back {
    top: 493px;
    background: var(--paper);
  }
  .front-brand {
    position: absolute;
    right: 54px;
    top: 206px;
    font-size: 44px;
    line-height: 1;
    color: var(--white);
    letter-spacing: 0.5px;
  }
  .front-web {
    position: absolute;
    right: 50px;
    top: 283px;
    font-size: 15px;
    color: var(--white);
    letter-spacing: 4.2px;
  }
  .back-brand {
    position: absolute;
    left: 52px;
    top: 84px;
    font-size: 30px;
    line-height: 1;
    color: var(--sky);
  }
  .contact {
    position: absolute;
    right: 50px;
    top: 186px;
    text-align: right;
  }
  .contact__name {
    font-family: "PT Sans", "Myriad Pro", sans-serif;
    font-weight: 700;
    font-size: 21px;
    color: var(--navy);
    line-height: 1.1;
  }
  .contact__name .surname { color: var(--sky); }
  .contact__title {
    font-size: 15px;
    color: var(--grey-text);
    margin-top: 2px;
  }
  .contact__list {
    list-style: none;
    margin-top: 14px;
  }
  .contact__item {
    font-size: 15px;
    color: var(--grey-text);
    line-height: 19.5px;
    display: flex;
    justify-content: flex-end;
    align-items: center;
    gap: 6px;
  }
  .contact__icon { width: 13px; height: 13px; fill: var(--navy); flex: none; }
</style>
</head>
<body>
  <section class="card card--front" aria-label="Card front">
    <div class="front-brand">Brightvale Global</div>
    <div class="front-web">www.brightvale.example</div>
  </section>

  <section class="card card--back" aria-label="Card back">
    <div class="back-brand">Brightvale Global</div>
    <div class="contact">
      <div class="contact__name">Marcus <span class="surname">Ortega</span></div>
      <div class="contact__title">CEO</div>
      <ul class="contact__list">
        <li class="contact__item">310-647-2093
          <svg class="contact__icon" viewBox="0 0 16 16" aria-hidden="true"><path d="M3.6 1.2l2.3 2.6-1.3 2a8.5 8.5 0 0 0 5.6 5.6l2-1.3 2.6 2.3-1.4 2.3C8 14.8 1.2 8 .9 2.6z"/></svg>
        </li>
        <li class="contact__item">bvgcorp7@mailnest.example
          <svg class="contact__icon" viewBox="0 0 16 16" aria-hidden="true"><path d="M1 3h14v1.2L8 9 1 4.2z M1 5.8l7 4.8 7-4.8V13H1z"/></svg>
        </li>
        <li class="contact__item">brightvale.example
          <svg class="contact__icon" viewBox="0 0 16 16" aria-hidden="true"><circle cx="8" cy="8" r="7"/><path d="M4 5c2 0 2 2 4 2s1 3 3 3M9 2c0 2 2 2 3 3" stroke="#f3f3f3" stroke-width="1.4" fill="none"/></svg>
        </li>
      </ul>
    </div>
  </section>
</body>
</html>
```